lantern pathway for children needs a website designer

We need a website designer for our new extension to our company known as 'lantern pathway' providing shadow support services to children based in Singapore. We are a sister branch of a private clinic 'Brightwell Learning' providing speech language, occupational, and educational therapy to children.

We would like to use our own photos. So the selected design should have a frame with pictures to give us an idea but we will replace them with our own. We will be needing help with inputting information and changing information throughout.

We would like to see designs that are simple, and professional. We have a logo (see attached). The result should convey professionalism in shadow support, fostering independent thinking and moving students towards self-learning.

Target Market(s)

Teachers, psychologists, parents

Industry/Entity Type

Clinic

Requirements
Should not have
• too distracting colours

```html
<!DOCTYPE html>
<html lang="en">
<head>
<meta charset="utf-8">
<title>Lantern Pathway</title>
<link href="https://fonts.googleapis.com/css2?family=Ubuntu:ital,wght@0,400;0,500;0,700;1,400&display=swap" rel="stylesheet">
<style>
:root{
  --brand:#7d0d0d;
  --brand-dark:#6a0808;
  --heading:#8a1414;
  --teal:#3f8f95;
  --purple:#94389a;
  --purple-dark:#7e2a86;
  --text:#4a4a4a;
  --muted:#8a8a8a;
  --pill:#e8e8e8;
  --line:#dcdcdc;
  --link:#7a1a6a;
}
*{box-sizing:border-box;margin:0;padding:0}
html,body{width:722px;height:1200px;overflow:hidden;background:#fff}
body{position:relative;font-family:'Ubuntu',sans-serif;color:var(--text)}
.abs{position:absolute}
.topline{left:0;top:0;width:722px;height:3px;background:var(--brand)}
.brand{left:90px;top:28px;display:flex;align-items:center;gap:8px}
.brand-dot{width:22px;height:22px;border-radius:50%;background:var(--brand)}
.brand-name{font-size:22px;font-weight:700;color:var(--brand)}
.email{left:514px;top:15px;font-size:9px;color:#888;display:flex;align-items:center;gap:4px}
.email-icon{width:12px;height:12px;border-radius:50%;background:#d7d7d7;display:flex;align-items:center;justify-content:center}
.nav{left:313px;top:48px;display:flex;gap:4px;list-style:none}
.nav li{height:17px;line-height:17px;padding:0 7px;border-radius:9px;background:var(--pill);font-size:8px;font-weight:700;color:#666;letter-spacing:.3px}
.nav li.active{background:var(--brand);color:#fff}
.hero-bg{left:0;top:82px;width:722px;height:250px;background:linear-gradient(180deg,#d9d9d9,#ececec 60%,#fff);clip-path:polygon(0 0,100% 0,100% 70%,0 100%)}
.slider{left:90px;top:93px;width:542px;height:258px;background:#fff;padding:8px;box-shadow:0 1px 6px rgba(0,0,0,.3)}
.slide-photo{position:absolute;left:8px;top:8px;width:526px;height:242px;background:linear-gradient(110deg,#c9a58a,#e3c9a8 45%,#9fb68a 80%,#6f9a5e)}
.slide-caption{position:absolute;left:8px;top:8px;width:200px;height:242px}
.slide-caption svg{position:absolute;left:0;top:0}
.caption-title{position:absolute;left:11px;top:21px;font-size:15px;font-weight:700;color:#fff;line-height:17px}
.caption-sub{position:absolute;left:11px;top:60px;font-size:9.5px;font-weight:700;color:#e4f3f2;line-height:11px}
.caption-body{position:absolute;left:14px;top:90px;width:140px;font-size:8px;color:#fff;line-height:14.5px}
.slide-arrows{position:absolute;left:18px;top:222px;color:#fff;font-size:13px;font-weight:700;letter-spacing:3px}
.services{left:90px;top:362px;width:542px;height:180px;background:linear-gradient(180deg,var(--purple),var(--purple-dark));box-shadow:0 6px 12px rgba(0,0,0,.25)}
.services-title{position:absolute;left:0;top:9px;width:100%;text-align:center;font-size:15px;font-weight:700;color:#e0b8df}
.services-title::before,.services-title::after{content:"";position:absolute;top:9px;width:175px;height:1px;background:#c58ac6}
.services-title::before{left:40px}.services-title::after{right:40px}
.service{position:absolute;top:40px;width:166px;text-align:center}
.service h3{font-size:10.5px;font-weight:400;color:#fff;margin-bottom:8px}
.service-photo{height:74px;border:2px solid #fff}
.service p{font-size:7.5px;color:#f1dcf1;margin-top:12px;line-height:10px}
.section-h{font-size:14px;font-weight:700;color:var(--heading)}
.welcome{left:90px;top:567px;width:540px}
.welcome p{font-size:7.8px;line-height:11px;margin-top:8px;color:#555}
.welcome p+p{margin-top:0}
.more{font-size:7.5px;font-style:italic;color:var(--link)}
.kids-bg{left:330px;top:640px;width:392px;height:240px;background:radial-gradient(ellipse at 70% 50%,#e9e9e9,#f7f7f7 55%,#fff 75%)}
.referrers{left:90px;top:669px;width:250px}
.referrers h4{font-size:10px;font-weight:500;color:#888;margin:12px 0 12px}
.referrers ul{list-style:none}
.referrers li{position:relative;padding-left:11px;font-size:7.8px;line-height:11px;color:#555;margin-bottom:8px}
.referrers li::before{content:"";position:absolute;left:0;top:3px;width:5px;height:5px;border-radius:50%;background:#999}
.video-h{left:367px;top:669px}
.video{left:370px;top:702px;width:258px;height:146px;background:#000;border:3px solid #ddd;border-radius:2px}
.shadow-bg{left:0;top:905px;width:722px;height:215px;background:radial-gradient(ellipse at 50% 40%,#ededed,#f8f8f8 60%,#fff)}
.divider{left:0;top:903px;width:722px;height:1px;background:var(--line)}
.pill-title{left:290px;top:886px;width:142px;height:32px;background:#fff;border:1px solid var(--line);border-radius:6px;text-align:center;line-height:30px}
.feature{position:absolute;top:945px;width:170px;text-align:center}
.feature h3{font-size:11.5px;font-weight:500;color:#333}
.feature p{font-size:7.8px;line-height:10.5px;color:#555;margin:8px 0 7px}
.newsletter{left:90px;top:1040px;width:542px;height:43px;background:#f4f4f4;border:1px solid #e2e2e2;display:flex;align-items:center;padding:0 12px}
.newsletter h3{font-size:14.5px;font-weight:400;color:#333;width:176px}
.newsletter .field{width:134px;height:18px;background:#fff;border:1px solid #ddd;font-size:7px;font-style:italic;color:#999;line-height:16px;padding-left:8px;margin-right:9px}
.newsletter .btn{margin-left:5px;height:18px;padding:0 6px;background:var(--brand);color:#fff;font-size:10px;line-height:18px}
.footer-line{left:0;top:1120px;width:722px;height:1px;background:var(--line)}
.foot-nav{left:90px;top:1136px;display:flex;gap:9px;font-size:7.5px;color:#555}
.address{left:90px;top:1152px;font-size:7.5px;color:#444}
.social{left:536px;top:1140px;display:flex;gap:4px}
.social span{width:15px;height:15px;border-radius:50%;background:#b5b5b5}
.bottom-bar{left:0;top:1176px;width:722px;height:24px;background:var(--brand-dark);color:#fff;font-size:7.5px;display:flex;align-items:center;justify-content:space-between;padding:0 91px 0 90px}
</style>
</head>
<body>
<div class="abs topline"></div>

<header>
  <div class="abs brand"><span class="brand-dot"></span><span class="brand-name">Lantern Pathway</span></div>
  <div class="abs email"><span class="email-icon"><svg width="7" height="5" viewBox="0 0 7 5"><rect x=".5" y=".5" width="6" height="4" fill="none" stroke="#777" stroke-width=".8"/><path d="M.5 .5 3.5 3 6.5 .5" fill="none" stroke="#777" stroke-width=".8"/></svg></span>hello@lanternpathway.example</div>
  <ul class="abs nav">
    <li class="active">HOME</li><li>ABOUT US</li><li>SERVICES</li><li>SHADOW SUPPORT</li><li>CONTACT US</li>
  </ul>
</header>

<div class="abs hero-bg" role="img" aria-label="Soft grey backdrop photo"></div>
<section class="abs slider">
  <div class="slide-photo" role="img" aria-label="Photo of a parent and child playing with shape puzzles at a table"></div>
  <div class="slide-caption">
    <svg width="200" height="242" viewBox="0 0 200 242"><path d="M0 0H175C140 40 150 90 160 130C170 175 150 215 120 242H0Z" fill="var(--teal)" opacity=".95"/></svg>
    <div class="caption-title">LANTERN PATHWAY<br>IS PART</div>
    <div class="caption-sub">of the Brightwell Learning<br>Group of Companies,</div>
    <div class="caption-body">Who are providing speech language therapy, occupational therapy and educational therapy services to both the Singapore and the international school community.</div>
    <div class="slide-arrows">&lsaquo; &rsaquo;</div>
  </div>
</section>

<section class="abs services">
  <h2 class="services-title">OUR SERVICES</h2>
  <div class="service" style="left:12px"><h3>Occupational Therapy</h3><div class="service-photo" role="img" aria-label="Photo of a therapist with a young girl" style="background:linear-gradient(120deg,#f2d9b8,#e9c48f 50%,#c7a07a)"></div><p>Brightwell Learning providing speech language therapy, occupational therapy.</p></div>
  <div class="service" style="left:188px"><h3>Educational Therapy</h3><div class="service-photo" role="img" aria-label="Photo of children reading with a teacher" style="background:linear-gradient(120deg,#d9c3a8,#b9b6c9 50%,#a6c08b)"></div><p>Brightwell Learning providing speech language therapy, occupational therapy.</p></div>
  <div class="service" style="left:364px"><h3>Speech Language Therapy</h3><div class="service-photo" role="img" aria-label="Photo of a boy studying at a desk" style="background:linear-gradient(120deg,#dfe6ee,#8fa9cf 50%,#d9d3cc)"></div><p>Brightwell Learning providing speech language therapy, occupational therapy.</p></div>
</section>

<section class="abs welcome">
  <h2 class="section-h">WELCOME TO LANTERN PATHWAY</h2>
  <p>Lantern Pathway is part of the Brightwell Learning Group of Companies, who are providing speech language therapy, occupational therapy and educational therapy services to both the Singapore and the international school community.</p>
  <p>Lantern Pathway aims to work in an integrated manner, respecting the work of the respective professionals involved and collaborating effectively.</p>
  <p class="more" style="margin-top:5px">&nbsp;Read more...</p>
</section>

<div class="abs kids-bg" role="img" aria-label="Faint photo of children learning"></div>

<section class="abs referrers">
  <h2 class="section-h">FOR REFERRERS</h2>
  <h4>How You Can Collaborate With Us</h4>
  <ul>
    <li>Shadow Support will participate in a collaborative working relationship with the professionals working with each student to facilitate progress</li>
    <li>Goals set out by professionals will be supported by the Shadow Support</li>
    <li>Frequent feedback and updates will be provided by the Shadow Support so that goals can remain relevant and up to date</li>
  </ul>
  <p class="more" style="position:absolute;left:205px;top:174px">Read more...</p>
</section>

<h2 class="abs section-h video-h">OUR VIDEO</h2>
<div class="abs video">
  <svg width="252" height="140" viewBox="0 0 252 140">
    <circle cx="120" cy="67" r="25" fill="none" stroke="#fff" stroke-width="2.5"/>
    <path d="M114 57 130 67 114 77Z" fill="#fff"/>
    <rect x="230" y="4" width="18" height="14" fill="#222"/><rect x="230" y="21" width="18" height="14" fill="#222"/><rect x="230" y="38" width="18" height="14" fill="#222"/><rect x="230" y="55" width="18" height="14" fill="#222"/>
    <circle cx="239" cy="28" r="4" fill="none" stroke="#fff" stroke-width="1.2"/>
    <path d="M235 11l4 3 4-3" fill="none" stroke="#fff" stroke-width="1.2"/>
    <path d="M236 47l6-6" stroke="#fff" stroke-width="1.2"/>
    <path d="M236 62l-2 2 2 2M242 62l2 2-2 2" fill="none" stroke="#fff" stroke-width="1"/>
    <rect x="0" y="120" width="252" height="20" fill="#111"/>
    <rect x="4" y="122" width="26" height="16" fill="#333"/>
    <path d="M13 126 21 130 13 134Z" fill="#fff"/>
    <rect x="38" y="128" width="156" height="4" fill="#444"/><rect x="38" y="128" width="48" height="4" fill="#1e7fb8"/>
    <rect x="198" y="127" width="20" height="6" fill="#1e7fb8"/>
    <text x="222" y="133" font-size="7" font-weight="700" fill="#1e7fb8" font-family="Ubuntu,sans-serif">HD</text>
    <path d="M238 126h4M238 126v4M248 134h-4M248 134v-4" stroke="#fff" stroke-width="1"/>
  </svg>
</div>

<div class="abs shadow-bg" role="img" aria-label="Faint photo of a child at school"></div>
<div class="abs divider"></div>
<div class="abs pill-title"><h2 class="section-h" style="line-height:30px">SHADOW SUPPORT</h2></div>

<section>
  <div class="feature" style="left:86px"><h3>What is shadow support?</h3><p>A shadow support is para-professional who can help a struggling student to integrate and learn in their school environment.</p><span class="more">Read more...</span></div>
  <div class="feature" style="left:281px"><h3>What are its Advantages?</h3><p>A fully trained shadow support is an asset to the student who otherwise would have trouble fitting in.</p><span class="more">Read more...</span></div>
  <div class="feature" style="left:468px"><h3>Child needs shadowing</h3><p>A consultation with our Speech Language Pathologist, along with an assessment by an Educational Psychologist.</p><span class="more">Read more...</span></div>
</section>

<form class="abs newsletter">
  <h3>Subscribe our newsletter</h3>
  <div class="field">Enter Your Name:</div>
  <div class="field">Enter Email address:</div>
  <div class="btn">Subscribe</div>
</form>

<footer>
  <div class="abs footer-line"></div>
  <nav class="abs foot-nav"><span>Home</span><span>About us</span><span>Services</span><span>Shadow support</span><span>Contact us</span></nav>
  <div class="abs address">412 Orchid Vale Road, #02-07 Maple Court Singapore 588210</div>
  <div class="abs social"><span></span><span></span><span></span><span></span><span></span></div>
  <div class="abs bottom-bar"><span>Copyright © 2014 Lantern Pathway.&nbsp; All Rights Reserved.</span><span>&#9990; 6123 - 4567 , 9876 - 5432</span></div>
</footer>
</body>
</html>
```